Hollow Covenant book cover.

Book cover design. Files must be in an accepted format by QWL Press for publishing.
Final book cover will need to be adjusted after acceptance. The spline anyway. Not the overall design.
Placement of bar code on back after design is done.
I can’t get the ISBN number until the cover is finalized.

Book blurb text on back
Title of the book is “Hollow Covenant.”

Book Blurb on back of cover below
Hollow covenant.
A fictional novel based on current events surrounding the covid 19 virous. Owen Pratley is a well-respected independent journalist contracted by the Harbor Ridge Ledger, upon his return from reporting on the war in Syria he is tasked to investigate the covid virus outbreak in China. As he digs deeper, he uncovers a hideous plot by the powers that be here in America. Owen risks life and limb to uncover the conspirators behind all of this and shed light to the American people.

```html
<!DOCTYPE html>
<html lang="en">
<head>
<meta charset="utf-8">
<title>Hollow Covenant — Book Cover</title>
<link rel="stylesheet" href="https://fonts.googleapis.com/css2?family=Playfair+Display:wght@400;500&family=Cardo&display=swap">
<style>
  :root {
    --ink-black: #050505;
    --back-night: #111418;
    --paper-white: #ffffff;
    --flag-blue: #1d2b66;
    --flag-red: #8e1520;
  }
  * { margin: 0; padding: 0; box-sizing: border-box; }
  html, body { width: 1200px; height: 869px; overflow: hidden; background: var(--ink-black); }
  .cover { position: relative; width: 1200px; height: 869px; overflow: hidden; background: var(--ink-black); }

  .back-photo {
    position: absolute; left: 0; top: 0; width: 576px; height: 869px;
    background: radial-gradient(ellipse 260px 340px at 230px 420px, #23272c 0%, var(--back-night) 55%, var(--ink-black) 100%);
  }
  .front-photo {
    position: absolute; left: 640px; top: 0; width: 560px; height: 869px;
    background:
      radial-gradient(ellipse 230px 330px at 400px 290px, #9a9a9a 0%, #5a5a5a 40%, transparent 75%),
      linear-gradient(180deg, var(--flag-blue) 0%, #2a2f5a 22%, var(--flag-red) 38%, #6a1018 62%, #1a1a1a 80%, var(--ink-black) 100%);
  }
  .spine-band { position: absolute; left: 576px; top: 0; width: 64px; height: 869px; background: var(--ink-black); }

  .type-layer { position: absolute; left: 0; top: 0; width: 1200px; height: 869px; overflow: hidden; }
  .title-text { font-family: "Playfair Display", serif; font-weight: 400; fill: var(--paper-white); }
  .title-group { filter: drop-shadow(1px 2px 0 #8a8a8a) drop-shadow(2px 4px 5px rgba(0,0,0,.85)); }
  .star { fill: var(--paper-white); }
  .author-text { font-family: "Playfair Display", serif; fill: var(--paper-white); }
  .spine-text { font-family: "Playfair Display", serif; fill: var(--paper-white); }

  .blurb { position: absolute; left: 62px; top: 307px; width: 449px; color: var(--paper-white);
    font-family: "Cardo", serif; font-size: 18.6px; line-height: 24.8px; }
  .blurb-heading { text-align: center; margin-bottom: 24px; }
  .blurb-body { text-align: justify; }

  .barcode-space { position: absolute; left: 318px; top: 698px; width: 212px; height: 130px; background: var(--paper-white); }
</style>
</head>
<body>
<main class="cover">
  <div class="back-photo" role="img" aria-label="Dark night photograph of the Capitol dome"></div>
  <div class="spine-band"></div>
  <div class="front-photo" role="img" aria-label="Black and white profile portrait of a man over a flag and Capitol building composite"></div>

  <div class="blurb">
    <p class="blurb-heading">Hollow covenant.</p>
    <p class="blurb-body">A fictional novel based on current events surrounding the covid 19 virus. Owen Pratley is a well-respected independent journalist contracted by the Harbor Ridge Ledger, upon his return from reporting on the war in Syria he is tasked to investigate the covid virus outbreak in China. As he digs deeper, he uncovers a hideous plot by the powers that be here in America. Owen risks life and limb to uncover the conspirators behind all of this and shed light to the American people.</p>
  </div>
  <div class="barcode-space"></div>

  <svg class="type-layer" viewBox="0 0 1200 869" width="1200" height="869">
    <defs>
      <polygon id="star" points="0,-11 2.6,-3.6 10.5,-3.4 4.2,1.4 6.5,9 0,4.6 -6.5,9 -4.2,1.4 -10.5,-3.4 -2.6,-3.6"/>
    </defs>

    <!-- Back title -->
    <g class="title-group">
      <use href="#star" class="star" transform="translate(190 140) scale(0.95)"/>
      <text class="title-text" x="306" y="156" font-size="51" text-anchor="middle" textLength="150" lengthAdjust="spacingAndGlyphs">HOLLOW</text>
      <use href="#star" class="star" transform="translate(412 140) scale(0.95)"/>
      <text class="title-text" x="306" y="244" font-size="93" text-anchor="middle" textLength="270" lengthAdjust="spacingAndGlyphs">COVENANT</text>
    </g>

    <!-- Spine -->
    <use href="#star" class="star" transform="translate(603 137) scale(1.45)"/>
    <text class="spine-text" transform="translate(617 350) rotate(-90)" font-size="32" text-anchor="middle" textLength="356" lengthAdjust="spacingAndGlyphs">HOLLOW COVENANT</text>
    <use href="#star" class="star" transform="translate(603 563) scale(1.45)"/>
    <text class="spine-text" transform="translate(612 714) rotate(-90)" font-size="13" text-anchor="middle" textLength="190" lengthAdjust="spacing">AUTHOR NAME</text>

    <!-- Front -->
    <text class="author-text" x="704" y="88" font-size="31" textLength="404" lengthAdjust="spacing" style="filter: drop-shadow(1px 2px 3px rgba(0,0,0,.8))">AUTHOR NAME</text>
    <g class="title-group">
      <use href="#star" class="star" transform="translate(745 646) scale(1.4)"/>
      <text class="title-text" x="916" y="672" font-size="79" text-anchor="middle" textLength="240" lengthAdjust="spacingAndGlyphs">HOLLOW</text>
      <use href="#star" class="star" transform="translate(1088 646) scale(1.4)"/>
      <text class="title-text" x="920" y="812" font-size="152" text-anchor="middle" textLength="420" lengthAdjust="spacingAndGlyphs">COVENANT</text>
    </g>
  </svg>
</main>
</body>
</html>
```